Talvern Asset Management - Corporate Letter Head Project

Looking for a classy design based on our current logo. Please find current logo source file in files. With our color scheme.

Target Market(s)

We're an investment firm, the letterhead needs to look professional and attractive to clients.

Industry/Entity Type

Hedgefund

Colors
0054AA
0677BA
7BADD7
CADEEF
E8F1F8

Requirements
Must have
• Our logo, address, phone number, and email

```html
<!DOCTYPE html>
<html lang="en">
<head>
<meta charset="UTF-8">
<title>Talvern Asset Management – Letterhead</title>
<link href="https://fonts.googleapis.com/css2?family=Lato:wght@400;700&family=Montserrat:wght@400;600&family=Dancing+Script:wght@500&display=swap" rel="stylesheet">
<style>
  :root {
    --navy: #1b2a4e;
    --paper: #ffffff;
    --backdrop: #e6e7e9;
    --ink: #2b2b2b;
    --ink-soft: #444444;
  }
  * { margin: 0; padding: 0; box-sizing: border-box; }
  html, body { width: 1200px; height: 874px; overflow: hidden; background: var(--backdrop); }
  .canvas { position: relative; width: 1200px; height: 874px; }
  .letterhead {
    position: absolute; left: 303px; top: 17px;
    width: 594px; height: 840px;
    background: var(--paper);
    box-shadow: 0 2px 10px rgba(0,0,0,0.12);
    overflow: hidden;
    font-family: 'Lato', sans-serif;
    color: var(--ink);
  }
  .header-wave, .footer-band { position: absolute; left: 0; width: 594px; }
  .header-wave { top: 0; height: 240px; }
  .footer-band { bottom: 0; height: 26px; }
  .brand {
    position: absolute; left: 34px; top: 126px;
    display: flex; align-items: center; gap: 10px;
  }
  .brand-mark { width: 26px; height: 26px; border: 1.5px solid #fff; }
  .brand-name {
    font-family: 'Lato', sans-serif; font-weight: 400;
    color: #fff; font-size: 15px; letter-spacing: 0.06em; text-transform: uppercase;
    line-height: 1.2; width: 140px;
  }
  .contact {
    position: absolute; left: 392px; top: 44px;
    font-family: 'Montserrat', sans-serif; font-style: normal; font-size: 8.5px; color: var(--ink);
    line-height: 1.45;
  }
  .contact-row { display: flex; align-items: center; gap: 5px; }
  .contact-row svg { width: 8px; height: 8px; fill: var(--navy); flex: none; }
  .contact-address { margin-bottom: 3px; }
  .letter { position: absolute; left: 62px; top: 262px; width: 460px; }
  .letter-date, .recipient { font-size: 10px; line-height: 1.35; color: var(--ink-soft); }
  .letter-date { margin-bottom: 10px; }
  .recipient { margin-bottom: 10px; }
  .salutation { font-family: 'Montserrat', sans-serif; font-weight: 600; font-size: 12px; margin-bottom: 10px; }
  .letter p { font-size: 9.6px; line-height: 1.38; color: var(--ink-soft); margin-bottom: 12px; }
  .closing { font-size: 10px; color: var(--ink-soft); margin-top: 18px; }
  .signature { font-family: 'Dancing Script', cursive; font-size: 30px; color: var(--ink); margin: 6px 0 0 24px; }
</style>
</head>
<body>
<div class="canvas">
  <article class="letterhead">
    <svg class="header-wave" viewBox="0 0 594 240" aria-hidden="true">
      <path fill="var(--navy)" d="M0,0 H594 V20 H410 C340,26 305,80 270,128 C232,182 150,206 0,212 Z"/>
      <path fill="none" stroke="#fff" stroke-width="5" d="M0,219 C155,213 240,190 278,134 C312,86 345,32 414,27 H594"/>
      <path fill="none" stroke="var(--navy)" stroke-width="1.6" d="M0,227 C160,221 248,196 286,140 C318,92 352,40 418,35"/>
    </svg>

    <div class="brand">
      <span class="brand-mark"></span>
      <span class="brand-name">Talvern Asset Management</span>
    </div>

    <address class="contact">
      <div class="contact-address">2240 Harwell Ave, Ste<br>100, Dallas, TX 75204</div>
      <div class="contact-row"><svg viewBox="0 0 10 10"><path d="M2,0.5 L4,2.5 L3,3.8 C3.6,5 5,6.4 6.2,7 L7.5,6 L9.5,8 L8,9.5 C4.5,9.5 0.5,5.5 0.5,2 Z"/></svg>555-014-2290</div>
      <div class="contact-row"><svg viewBox="0 0 10 10"><path d="M0,2 H10 V8 H0 Z M0,2 L5,5.5 L10,2" stroke="#fff" stroke-width="0.8"/></svg>info@talvernasset.com</div>
      <div class="contact-row"><svg viewBox="0 0 10 10"><circle cx="5" cy="5" r="4.6"/></svg>www.talvernasset.com</div>
    </address>

    <section class="letter">
      <div class="letter-date">Feb-03-2022</div>
      <div class="recipient">Mr. John Doe<br>President</div>
      <div class="recipient">Calderwick Corporation<br>123 Street Name, Suite# 10<br>City, State, 120023</div>
      <div class="salutation">Dear Mr. John</div>
      <p>Lorem ipsum dolor sit amet, consectetur adipisicing elit, sed do eiusmod tempor incididunt ut labore et dolore magna aliqua. Ut enim ad minim veniam, quis nostrud exercitation ullamco laboris nisi ut aliquip ex ea commodo consequat. Duis aute irure dolor in reprehenderit in voluptate velit esse cillum dolore eu fugiat nulla pariatur.</p>
      <p>Lorem ipsum dolor sit amet, consectetur adipisicing elit, sed do eiusmod tempor incididunt ut labore et dolore magna aliqua. Ut enim ad minim veniam, quis nostrud exercitation ullamco laboris nisi ut aliquip ex ea commodo consequat. Duis aute irure dolor in reprehenderit in voluptate velit esse cillum dolore eu fugiat nulla pariatur.</p>
      <p>Lorem ipsum dolor sit amet, consectetur adipisicing elit, sed do eiusmod tempor incididunt ut labore et dolore magna aliqua. Ut enim ad minim veniam, quis nostrud exercitation ullamco laboris nisi ut aliquip ex ea commodo consequat.</p>
      <p>Excepteur sint occaecat cupidatat non proident, sunt in culpa qui officia deserunt mollit anim id est laborum. re et dolore magnam aliquam quaerat voluptatem.</p>
      <div class="closing">Regards</div>
      <div class="signature">Daniel Reeve</div>
    </section>

    <svg class="footer-band" viewBox="0 0 594 26" aria-hidden="true">
      <rect x="0" y="6" width="594" height="20" fill="var(--navy)"/>
      <polygon points="440,6 446,6 458,26 452,26" fill="#fff"/>
    </svg>
  </article>
</div>
</body>
</html>
```